Update, redesign www.quorvel.net. Put it on WordPress and migrate to new host site

My current website is www.quorvel.net. The text content is ok but the site look and feel is several years old and does not project a sense of innovation. I am looking for a more modern exciting look. It needs to be built on word press and I need help in in putting it with a new hosting service.
Updates

Went on vacation/holiday

Target Market(s)

Established organizations

Industry/Entity Type

Business Consultant

Number of Pages Required

1 page

Font styles to use
Sans Serif

Colors

Designer to choose colors to be used in the design.

Requirements
Must have
• Simple. Easy to read and navigate
Nice to have
• Innovation, creativity especially the leadership of innovation. Reading the current text on www.quorvel.net should help you with ideas
Should not have
• Difficulty in me managing or adding content after it is built

```html
<!DOCTYPE html>
<html lang="en">
<head>
<meta charset="utf-8">
<title>Quorvel — Innovation at Work</title>
<link rel="stylesheet" href="https://fonts.googleapis.com/css2?family=Montserrat:wght@400;500;600;700&family=Raleway:wght@400;500;700;800&display=swap">
<style>
:root{
  --red:#ef333d;
  --ink:#222428;
  --text:#4a4a4a;
  --muted:#7a7a7a;
  --line:#e4e4e4;
  --band:#f6f6f6;
  --hero-dark:#1d1d1f;
  --white:#ffffff;
}
*{margin:0;padding:0;box-sizing:border-box}
html,body{width:1200px;height:2419px;overflow:hidden}
body{position:relative;background:var(--white);font-family:'Montserrat',sans-serif;color:var(--text)}
.abs{position:absolute}

/* header */
.site-header{left:0;top:0;width:1200px;height:52px;background:var(--white)}
.brand{left:113px;top:8px;display:flex;align-items:baseline;gap:14px}
.brand-name{font-family:'Raleway',sans-serif;font-weight:800;font-size:30px;color:var(--red);line-height:1}
.brand-tag{font-size:12px;color:var(--muted)}
.nav a{position:absolute;top:17px;font-size:12px;color:var(--ink);text-decoration:none}
.nav-cta{left:979px;top:8px;width:113px;height:31px;background:var(--red);color:var(--white);font-size:11px;font-weight:600;display:flex;align-items:center;justify-content:center;border-radius:2px}

/* hero */
.hero{left:0;top:52px;width:1200px;height:566px;background:linear-gradient(90deg,#1b1b1d 0%,#222224 45%,#3a3a3c 70%,#555 100%)}
.hero-photo{left:640px;top:0;width:560px;height:566px;background:radial-gradient(ellipse at 60% 40%,#6b6b6b 0%,#3b3b3d 55%,rgba(34,34,36,0) 100%)}
.hero-kicker{left:120px;top:142px;font-family:'Raleway',sans-serif;font-size:32px;letter-spacing:3px;color:var(--red);font-weight:500}
.hero-title{left:118px;top:184px;font-family:'Raleway',sans-serif;font-size:48px;font-weight:800;color:var(--white)}
.hero-rule{left:126px;top:273px;width:56px;height:3px;background:var(--white)}
.hero-lede{left:127px;top:308px;width:500px;font-size:21px;line-height:30px;color:var(--white)}

/* clients band */
.clients{left:0;top:618px;width:1200px;height:113px;background:var(--band)}
.client-badge{top:44px;height:24px;background:#cfcfcf;border-radius:3px}

/* services */
.section-title{width:1200px;left:0;text-align:center;font-family:'Montserrat',sans-serif;font-weight:600;font-size:25px;color:var(--ink)}
.section-title .accent{color:var(--red)}
.title-rule{left:582px;width:36px;height:3px;background:var(--ink)}
.service-card{top:852px;height:238px;background:var(--white);border:1px solid var(--line);box-shadow:0 1px 3px rgba(0,0,0,.06);text-align:center;padding:0 26px}
.service-card.featured{top:855px;height:261px;background:var(--red);border:none;box-shadow:0 6px 14px rgba(0,0,0,.18);color:var(--white)}
.service-icon{margin:28px auto 0;display:block}
.service-name{font-size:15px;font-weight:700;color:var(--ink);margin-top:10px;line-height:20px}
.service-desc{font-size:10px;line-height:17px;color:var(--text);margin-top:14px}
.service-more{font-size:10px;font-weight:600;color:var(--red);margin-top:20px;display:block}
.featured .service-name,.featured .service-desc,.featured .service-more{color:var(--white)}

/* book promo */
.promo{left:0;top:1182px;width:1200px;height:479px;background:linear-gradient(180deg,#ececec 0%,#e2e2e2 70%,#d9d9d9 100%)}
.promo-scene{left:0;top:110px;width:320px;height:369px;background:linear-gradient(180deg,rgba(210,210,210,0) 0%,#cfcfcf 100%)}
.book-cover{left:315px;top:70px;width:250px;height:340px;background:var(--red);box-shadow:6px 6px 14px rgba(0,0,0,.25)}
.promo-panel{left:594px;top:150px;width:600px;height:200px;background:rgba(255,255,255,.55)}
.promo-title{left:626px;top:134px;font-size:29px;font-weight:600;color:var(--ink)}
.promo-text{left:626px;top:182px;width:450px;font-size:13.5px;line-height:25px;color:var(--muted)}
.promo-btn{left:623px;top:291px;width:106px;height:29px;background:var(--red);color:var(--white);font-size:11px;font-weight:600;display:flex;align-items:center;justify-content:center;border-radius:2px}
.promo-next{left:1112px;top:216px}

/* about */
.about{left:0;top:1661px;width:1200px;height:275px;border-bottom:1px solid var(--line)}
.about-brand{left:161px;top:106px;font-family:'Raleway',sans-serif;font-weight:800;font-size:44px;color:var(--red);line-height:1}
.about-text{left:444px;top:79px;width:600px;font-size:14.5px;line-height:30.5px;color:var(--muted)}

/* contact */
.contact-item{top:2062px;width:200px;text-align:center;font-size:11.5px;color:var(--ink)}
.contact-item svg{display:block;margin:0 auto 12px}
.field{background:var(--white);border:1px solid var(--line);font-size:11px;color:var(--ink);padding:11px 16px}

/* footer */
.footer-rule{left:247px;width:697px;height:1px;background:#cfcfcf}
.footer-nav a{position:absolute;top:2352px;font-size:9.5px;color:var(--ink);text-decoration:none}
.copyright{left:0;top:2383px;width:1200px;text-align:center;font-size:8.5px;font-weight:600;color:var(--ink)}
</style>
</head>
<body>

<header class="site-header abs">
  <div class="brand abs"><span class="brand-name">quorvel</span><span class="brand-tag">Innovation at Work</span></div>
  <nav class="nav">
    <a style="left:559px">About</a>
    <a style="left:637px">Thoughts Leadership</a>
    <a style="left:795px">Services</a>
    <a style="left:892px">Videos</a>
  </nav>
  <a class="nav-cta abs">Get in Touch</a>
</header>

<section class="hero abs">
  <div class="hero-photo abs" role="img" aria-label="Monochrome photograph of a stone statue of a seated thinker against a building"></div>
  <p class="hero-kicker abs">Innovation at Work</p>
  <h1 class="hero-title abs">With Creative Team</h1>
  <div class="hero-rule abs"></div>
  <p class="hero-lede abs">Lorem ipsum dolor sit amet, consectetuer adipiscing elit. Aenean commodo</p>
</section>

<section class="clients abs" aria-label="Client badges">
  <div class="client-badge abs" style="left:30px;width:72px"></div>
  <div class="client-badge abs" style="left:132px;width:98px"></div>
  <div class="client-badge abs" style="left:273px;width:74px;border-radius:12px"></div>
  <div class="client-badge abs" style="left:390px;top:36px;width:40px;height:40px;border-radius:50%"></div>
  <div class="client-badge abs" style="left:497px;width:92px"></div>
  <div class="client-badge abs" style="left:609px;width:70px"></div>
  <div class="client-badge abs" style="left:737px;width:50px"></div>
  <div class="client-badge abs" style="left:847px;width:86px;height:16px;top:48px"></div>
  <div class="client-badge abs" style="left:987px;width:74px"></div>
  <div class="client-badge abs" style="left:1125px;width:58px"></div>
</section>

<h2 class="section-title abs" style="top:774px"><span class="accent">Quorvel</span> Services</h2>
<div class="title-rule abs" style="top:814px"></div>

<article class="service-card abs" style="left:107px;width:227px">
  <svg class="service-icon" width="40" height="48" viewBox="0 0 40 48" fill="none" stroke="var(--red)" stroke-width="2"><circle cx="20" cy="18" r="14"/><path d="M20 10l2.5 5 5.5.8-4 3.9 1 5.5-5-2.6-5 2.6 1-5.5-4-3.9 5.5-.8z"/><path d="M11 29l-5 15 7-3 4 6 3-11M29 29l5 15-7-3-4 6-3-11"/></svg>
  <h3 class="service-name">Consulting</h3>
  <p class="service-desc">When it comes to 'quality', there is no middle ground. At Veltra Health Inc. there is no concession...</p>
  <span class="service-more">Read more</span>
</article>

<article class="service-card featured abs" style="left:334px;width:271px">
  <svg class="service-icon" width="48" height="48" viewBox="0 0 48 48" fill="none" stroke="var(--white)" stroke-width="2"><circle cx="24" cy="24" r="21"/><rect x="16" y="22" width="16" height="12" rx="1"/><path d="M19 22v-4a5 5 0 0110 0v4"/><circle cx="24" cy="28" r="1.5"/></svg>
  <h3 class="service-name">Executive<br>Education</h3>
  <p class="service-desc">Information Security which is also known as data security is one of the main priorities or parameteu...</p>
  <span class="service-more">Read more</span>
</article>

<article class="service-card abs" style="left:605px;width:229px">
  <svg class="service-icon" width="40" height="46" viewBox="0 0 40 46" fill="none" stroke="var(--red)" stroke-width="2"><rect x="6" y="2" width="16" height="7" rx="1"/><path d="M8 9v5l-4 5v24h20V19l-4-5V9"/><path d="M4 26h20"/><rect x="22" y="30" width="16" height="10" rx="5" transform="rotate(-25 30 35)"/></svg>
  <h3 class="service-name">Books</h3>
  <p class="service-desc">When it comes to 'quality', there is no middle ground. At Veltra Health Inc. there is no concession...</p>
  <span class="service-more">Read more</span>
</article>

<article class="service-card abs" style="left:834px;width:244px">
  <svg class="service-icon" width="38" height="48" viewBox="0 0 38 48" fill="none" stroke="var(--red)" stroke-width="2"><rect x="3" y="6" width="32" height="40" rx="2"/><rect x="12" y="2" width="14" height="7" rx="1"/><path d="M9 19l2 2 4-4M9 28l2 2 4-4M9 37l2 2 4-4M19 19h10M19 28h10M19 37h10"/></svg>
  <h3 class="service-name">Speaking</h3>
  <p class="service-desc">When it comes to 'quality', there is no middle ground. At Veltra Health Inc. there is no concession...</p>
  <span class="service-more">Read more</span>
</article>

<section class="promo abs">
  <div class="promo-scene abs" role="img" aria-label="Photo of a potted plant, reading glasses and a stack of books on a white shelf"></div>
  <div class="book-cover abs" role="img" aria-label="Cover of the book Insight Dojo by Dana Whitlow"></div>
  <div class="promo-panel abs"></div>
  <h2 class="promo-title abs">Order Insight Dojo</h2>
  <p class="promo-text abs">Insight Dojo reveals 7 secret principles that can help any innovator overcome the roadblocks and blockheads that they will inevitably meet on the path to creativity</p>
  <a class="promo-btn abs">Buy Now</a>
  <svg class="promo-next abs" width="46" height="46" viewBox="0 0 46 46" fill="none" stroke="var(--ink)" stroke-width="1.5"><circle cx="23" cy="23" r="21"/><path d="M20 16l7 7-7 7" stroke-width="2"/></svg>
</section>

<section class="about abs">
  <div class="about-brand abs">quorvel</div>
  <p class="about-text abs">Quorvel works with a broad range of national and global clients to utilize "Innovation at Work" to improve business results. We help individuals and organizations through the entire value chain of innovation from idea generation, implementation and value creation.</p>
</section>

<h2 class="section-title abs" style="top:1987px"><span class="accent">Get in</span> Touch</h2>
<div class="title-rule abs" style="top:2026px"></div>

<div class="contact-item abs" style="left:307px">
  <svg width="20" height="26" viewBox="0 0 20 26"><path d="M10 0a9.5 9.5 0 00-9.5 9.5C.5 17 10 26 10 26s9.5-9 9.5-16.5A9.5 9.5 0 0010 0z" fill="var(--red)"/><circle cx="10" cy="9.5" r="3.5" fill="#fff"/></svg>
  2210 N Harbor Lane
</div>
<div class="contact-item abs" style="left:497px">
  <svg width="24" height="26" viewBox="0 0 24 26"><rect x="1" y="6" width="22" height="16" rx="1" fill="var(--red)"/><path d="M2 8l10 7 10-7" fill="none" stroke="#fff" stroke-width="1.6"/></svg>
  support@quorvel.net
</div>
<div class="contact-item abs" style="left:669px">
  <svg width="22" height="26" viewBox="0 0 22 26"><path d="M5 3l4 0 2 6-3 2c1.5 3.5 3.5 5.5 7 7l2-3 6 2v4c0 1.5-1.5 3-3 3C10 24 1 15 1 7c0-2 2-4 4-4z" fill="var(--red)"/></svg>
  (555) 214 - 0187
</div>

<form aria-label="Contact form">
  <div class="field abs" style="left:223px;top:2141px;width:364px;height:38px">Name</div>
  <div class="field abs" style="left:223px;top:2200px;width:364px;height:39px">Email</div>
  <div class="field abs" style="left:223px;top:2262px;width:364px;height:38px">Subject</div>
  <div class="field abs" style="left:605px;top:2141px;width:365px;height:159px">Message</div>
</form>

<footer>
  <div class="footer-rule abs" style="top:2344px"></div>
  <nav class="footer-nav">
    <a style="left:373px">About</a>
    <a style="left:437px">Thoughts Leadership</a>
    <a style="left:569px">Services</a>
    <a style="left:647px">Videos</a>
    <a style="left:740px">Get in Touch</a>
  </nav>
  <div class="footer-rule abs" style="top:2373px"></div>
  <p class="copyright abs">All rights reserved &nbsp;| &nbsp;Privacy Policy &nbsp;| &nbsp;Terms</p>
</footer>

</body>
</html>
```